Vyntra Ad Design for Culinary Toursim Company

Looking for ad design for www.savorlanewalks.example to be used on VYNTRA traffic ads.

Below is one example of the

We are looking for vyntra ad design
Post: 1080x1080 with text,
Stories: 1080x1920 with text

Text should read
Food For Thought
CTA: Join our {CITY} Food Tour

Logo and optional photos are attached. You can edit the photos as you see fit.
Brand guidelines https://www.filevault.example/s/k3m9q2x7/Savor-Lane-Walks-Brand-Guidelines.docx

Logos https://www.filevault.example/f/r8t4w1z6/logos

Target Market(s)

United States Foodies ages 30-65

Industry/Entity Type

Tourism

Font styles to use
Other font styles liked:
• Avenir

Requirements
Must have
• High Design
Nice to have
• See Brand Guidelines
Should not have
• See Brand Guidelines

```html
<!DOCTYPE html>
<html lang="en">
<head>
<meta charset="utf-8">
<title>Food For Thought – Tokyo Food Tour Ads</title>
<link rel="stylesheet" href="https://fonts.googleapis.com/css2?family=Montserrat:wght@500;700;800;900&display=swap">
<style>
  :root {
    --board: #595959;
    --paper: #f3f3f2;
    --paper-shade: #e4e4e3;
    --red: #b0141c;
    --red-deep: #8f0f15;
    --ink: #2a2a2a;
    --grey-line: #9a9a9a;
    --sky-top: #1d3457;
    --sky-mid: #4a6c98;
    --sky-glow: #d9a15f;
  }
  * { margin: 0; padding: 0; box-sizing: border-box; }
  html, body { width: 1200px; height: 2956px; overflow: hidden; }
  body {
    background: var(--board);
    font-family: "Montserrat", "Avenir", sans-serif;
    position: relative;
  }
  .ad {
    position: absolute;
    overflow: hidden;
    background:
      radial-gradient(ellipse at 30% 60%, #ffffff 0%, var(--paper) 50%, var(--paper-shade) 100%);
  }
  .ad--post { left: 136px; top: 112px; width: 928px; height: 1040px; }
  .ad--story { left: 208px; top: 1312px; width: 784px; height: 1392px; }

  .hero-photo {
    position: absolute; left: 0; top: 0; width: 100%;
    background: linear-gradient(180deg, var(--sky-top) 0%, var(--sky-mid) 45%, var(--sky-glow) 80%, #7a4a2e 100%);
  }
  .ad--post .hero-photo {
    height: 360px;
    clip-path: polygon(0 0,100% 0,100% 78%,88% 84%,74% 80%,62% 88%,50% 84%,42% 96%,34% 90%,26% 100%,18% 92%,8% 98%,0 90%);
  }
  .ad--story .hero-photo {
    height: 430px;
    clip-path: polygon(0 0,100% 0,100% 82%,86% 86%,72% 82%,60% 90%,48% 86%,40% 97%,30% 91%,22% 100%,12% 93%,0 96%);
  }

  .brush-red {
    position: absolute; right: 0; bottom: 0; fill: var(--red);
  }

  .route-line {
    position: absolute; fill: none; stroke: var(--red); stroke-width: 3; stroke-dasharray: 10 8;
  }

  .polaroid {
    position: absolute; background: #fff; padding: 12px;
    box-shadow: 0 8px 18px rgba(0,0,0,.35);
  }
  .polaroid .photo { width: 100%; height: 100%; }
  .photo--market { background: linear-gradient(135deg, #3f6a34 0%, #c98a3a 45%, #3a2b22 100%); }
  .photo--vendor { background: linear-gradient(160deg, #6b4a2f 0%, #b7362a 40%, #2f5a2c 75%, #1e1a17 100%); }
  .photo--stall  { background: linear-gradient(180deg, #5a3a24 0%, #a8432d 40%, #c99a55 70%, #3e2b1e 100%); }

  .headline {
    position: absolute; font-weight: 900; text-transform: uppercase; line-height: 1;
  }
  .headline .red { color: var(--red); }
  .headline .ink { color: var(--ink); }
  .cta { position: absolute; text-transform: uppercase; font-weight: 900; line-height: 1; }
  .cta .join { color: var(--red); font-weight: 800; letter-spacing: 1px; }
  .cta .city { color: var(--ink); }
  .cta .tour { color: var(--red); }

  .brand {
    position: absolute; display: flex; align-items: center; gap: 10px;
    color: var(--ink); font-weight: 500; font-size: 22px;
  }
  .brand .dot { width: 18px; height: 18px; border-radius: 50%; background: var(--red); }

  .pin { position: absolute; fill: none; stroke: var(--grey-line); stroke-width: 3; }
</style>
</head>
<body>

<!-- Square post -->
<section class="ad ad--post">
  <div class="hero-photo" role="img" aria-label="Red Japanese pagoda against a twilight sky over Tokyo"></div>

  <svg class="brush-red" width="340" height="300" viewBox="0 0 340 300">
    <path d="M340 0 L300 30 L260 20 L240 60 L200 70 L190 110 L150 130 L140 170 L100 190 L90 230 L40 250 L0 300 L340 300 Z"/>
  </svg>

  <svg class="route-line" style="left:420px;top:250px" width="200" height="620" viewBox="0 0 200 620">
    <path d="M180 0 C60 80 40 200 120 300 C190 390 40 460 60 620"/>
  </svg>

  <div class="polaroid" style="left:580px;top:95px;width:270px;height:250px;transform:rotate(3deg)">
    <div class="photo photo--market" role="img" aria-label="Tour guide at a colourful produce market"></div>
  </div>
  <div class="polaroid" style="left:540px;top:360px;width:270px;height:240px;transform:rotate(-2deg)">
    <div class="photo photo--vendor" role="img" aria-label="Street food vendor preparing a dish"></div>
  </div>
  <div class="polaroid" style="left:580px;top:620px;width:250px;height:250px;transform:rotate(2deg)">
    <div class="photo photo--stall" role="img" aria-label="Market stall with jars of spices and pickles"></div>
  </div>

  <h1 class="headline" style="left:72px;top:470px">
    <span class="red" style="display:block;font-size:66px">Food for</span>
    <span class="ink" style="display:block;font-size:66px;margin-top:6px">Thought</span>
  </h1>

  <p class="cta" style="left:120px;top:660px;text-align:center;width:340px">
    <span class="join" style="display:block;font-size:30px">Join our</span>
    <span class="city" style="display:block;font-size:78px;margin-top:8px">Tokyo</span>
    <span class="tour" style="display:block;font-size:46px;margin-top:6px">Food Tour</span>
  </p>

  <div class="brand" style="left:90px;top:920px">
    <span class="dot"></span><span>Savor Lane Walks</span>
  </div>

  <svg class="pin" style="left:430px;top:900px" width="36" height="50" viewBox="0 0 36 50">
    <path d="M18 47 C18 47 4 28 4 18 A14 14 0 0 1 32 18 C32 28 18 47 18 47 Z"/>
    <circle cx="18" cy="18" r="5"/>
  </svg>
</section>

<!-- Story -->
<section class="ad ad--story">
  <div class="hero-photo" role="img" aria-label="Red Japanese pagoda against a twilight sky over Tokyo"></div>

  <svg class="brush-red" width="420" height="640" viewBox="0 0 420 640">
    <path d="M420 0 L380 40 L350 30 L330 90 L300 110 L290 180 L250 210 L240 290 L200 320 L190 400 L150 430 L140 510 L90 540 L60 600 L0 640 L420 640 Z"/>
  </svg>

  <svg class="route-line" style="left:300px;top:420px" width="180" height="860" viewBox="0 0 180 860">
    <path d="M160 0 C40 120 20 260 110 380 C180 480 30 600 60 860"/>
  </svg>

  <div class="polaroid" style="left:392px;top:150px;width:360px;height:280px;transform:rotate(3deg)">
    <div class="photo photo--market" role="img" aria-label="Tour guide at a colourful produce market"></div>
  </div>
  <div class="polaroid" style="left:400px;top:470px;width:340px;height:260px;transform:rotate(-2deg)">
    <div class="photo photo--vendor" role="img" aria-label="Street food vendor preparing a dish"></div>
  </div>
  <div class="polaroid" style="left:392px;top:790px;width:350px;height:320px;transform:rotate(2deg)">
    <div class="photo photo--stall" role="img" aria-label="Market stall with jars of spices and pickles"></div>
  </div>

  <h1 class="headline" style="left:60px;top:570px;width:300px;text-align:center">
    <span class="red" style="display:block;font-size:84px">Food</span>
    <span class="red" style="display:block;font-size:44px;margin-top:8px">For</span>
    <span class="ink" style="display:block;font-size:62px;margin-top:8px">Thought</span>
  </h1>

  <p class="cta" style="left:50px;top:860px;width:320px;text-align:center">
    <span class="join" style="display:block;font-size:30px">Join our</span>
    <span class="city" style="display:block;font-size:78px;margin-top:10px">Tokyo</span>
    <span class="tour" style="display:block;font-size:44px;margin-top:8px">Food Tour</span>
  </p>

  <div class="brand" style="left:90px;top:1200px">
    <span class="dot"></span><span>Savor Lane Walks</span>
  </div>

  <svg class="pin" style="left:356px;top:1250px" width="36" height="50" viewBox="0 0 36 50">
    <path d="M18 47 C18 47 4 28 4 18 A14 14 0 0 1 32 18 C32 28 18 47 18 47 Z"/>
    <circle cx="18" cy="18" r="5"/>
  </svg>
</section>

</body>
</html>
```